Massage Therapy and Personal Training Business Card (Lorvex Wellness)

I need a logo design based in Washington. The company is called Lorvex Wellness. Lorvex are my initials. I specialize in massage therapy and personal training and general wellness of my clients. I've tried getting designs but haven't quite yet found what I'm looking for. I'm not inclined to a certain color yet but some color that resembles wellness such as light blue and white or green and white. Again, I'm not really picky about that. Thank you in advance

Industry/Entity Type

Business

Contact Information for Business Card

Have the description on one side and space for writing information on the back side such as number, appt, etc. I have an example attached. I see a lot of these card. I dont want the exact one, but something similar. Simple, professional and elegant.

Colors

Designer to choose colors to be used in the design.

Requirements
Must have
• Space on the back side to write
• A professional, elegant look
Should not have
• cartoon like style.

```html
<!DOCTYPE html>
<html lang="en">
<head>
<meta charset="utf-8">
<title>Lorvex Wellness – Business Card</title>
<link rel="stylesheet" href="https://fonts.googleapis.com/css2?family=Cinzel:wght@400&family=Open+Sans:wght@400;600&display=swap">
<style>
  :root {
    --green: #5a9a36;
    --ink: #3a3a3a;
    --line: #333333;
    --card: #ffffff;
    --backdrop: #e9e7e3;
    --figure-light: #f3f3f3;
    --figure-mid: #d6d6d6;
  }
  * { margin: 0; padding: 0; box-sizing: border-box; }
  html, body { width: 1200px; height: 1000px; overflow: hidden; }
  body {
    background: var(--backdrop);
    position: relative;
    font-family: "Open Sans", Arial, sans-serif;
    color: var(--ink);
  }
  .card {
    position: absolute;
    left: 266px;
    width: 666px;
    background: var(--card);
    border-radius: 24px;
    overflow: hidden;
    box-shadow: 0 4px 14px rgba(0,0,0,0.18);
  }
  .card--front { top: 75px; height: 395px; }
  .card--back { top: 533px; height: 397px; }

  .anatomy-figure {
    position: absolute;
    left: 336px; top: 0;
    width: 310px; height: 372px;
    background: radial-gradient(ellipse at 50% 45%, var(--figure-light) 0%, var(--figure-mid) 65%, #ffffff 100%);
  }
  .front-band { position: absolute; left: 0; top: 335px; width: 666px; height: 60px; }

  .brand-mark {
    position: absolute; left: 132px; top: 44px;
    width: 84px; height: 84px;
  }
  .brand { position: absolute; left: 0; width: 348px; text-align: center; }
  .brand__name {
    top: 150px;
    font-family: "Cinzel", "Times New Roman", serif;
    font-size: 29px;
    line-height: 36px;
    color: var(--green);
    white-space: nowrap;
  }
  .brand__tagline { top: 185px; font-size: 19px; color: var(--ink); }
  .contact { position: absolute; left: 0; width: 348px; text-align: center; }
  .contact__name { top: 233px; font-size: 18px; color: var(--green); }
  .contact__role { top: 255px; font-size: 16px; }
  .contact__phone { top: 286px; font-size: 16px; }
  .contact__email { top: 308px; font-size: 16px; }

  .appointment__title {
    position: absolute; top: 28px; left: 0; width: 666px; text-align: center;
    font-size: 19px; font-weight: 600; color: var(--green); word-spacing: 3px;
  }
  .write-line { position: absolute; left: 136px; width: 394px; height: 2px; background: var(--line); }
  .write-line--name { top: 132px; }
  .write-line--datetime { top: 264px; }
  .field-label {
    position: absolute; font-size: 16px; font-weight: 600; color: var(--green);
    transform: translateX(-50%);
  }
  .field-label--name { top: 140px; left: 333px; }
  .field-label--date { top: 272px; left: 242px; }
  .field-label--time { top: 272px; left: 425px; }
  .day {
    position: absolute; top: 190px;
    display: flex; align-items: center; gap: 14px;
    font-size: 16px; font-weight: 600; color: var(--green);
  }
  .day__box {
    width: 26px; height: 19px; border: 2px solid var(--line); border-radius: 5px;
  }
  .policy { position: absolute; left: 0; width: 666px; text-align: center; font-size: 16.6px; }
  .policy__title { top: 324px; }
  .policy__text { top: 348px; }
</style>
</head>
<body>

<section class="card card--front">
  <div class="anatomy-figure" role="img" aria-label="Grey anatomical illustration of a human back and shoulder muscles with green highlight circles"></div>
  <svg class="front-band" viewBox="0 0 666 60" aria-hidden="true">
    <path d="M0 12 Q333 62 666 10 L666 60 L0 60 Z" fill="var(--green)"/>
  </svg>

  <svg class="brand-mark" viewBox="0 0 84 84" aria-hidden="true">
    <circle cx="42" cy="42" r="39" fill="none" stroke="var(--green)" stroke-width="3"/>
  </svg>
  <div class="brand brand__name">LORVEX WELLNESS</div>
  <div class="brand brand__tagline">Message Therapy</div>

  <div class="contact contact__name">DANIEL MERCER</div>
  <div class="contact contact__role">Massage Therapist</div>
  <div class="contact contact__phone">0418 265 903</div>
  <div class="contact contact__email">daniel@lorvexwellness.com</div>
</section>

<section class="card card--back">
  <h2 class="appointment__title">YOUR NEXT APPOINTMENT</h2>

  <div class="write-line write-line--name"></div>
  <div class="field-label field-label--name">NAME</div>

  <div class="day" style="left:32px">Mon <span class="day__box"></span></div>
  <div class="day" style="left:142px">Tue <span class="day__box"></span></div>
  <div class="day" style="left:245px">Wed <span class="day__box"></span></div>
  <div class="day" style="left:356px">Thur <span class="day__box"></span></div>
  <div class="day" style="left:472px">Fri <span class="day__box"></span></div>
  <div class="day" style="left:568px">Sat <span class="day__box"></span></div>

  <div class="write-line write-line--datetime"></div>
  <div class="field-label field-label--date">DATE</div>
  <div class="field-label field-label--time">TIME</div>

  <div class="policy policy__title">CANCELATION POLICY</div>
  <div class="policy policy__text">If you are unable to keep your appointment , please allow 24 hours notice</div>
</section>

</body>
</html>
```